PowerPoint template for my training workshop business

I would like to have a PowerPoint template created using my logo and palette materials created by Brivantelox. I train and facilitate workshops using PowerPoint in both corporate and public settings.

I have attached the original design elements to this request.

```html
<!DOCTYPE html>
<html lang="en">
<head>
<meta charset="utf-8">
<title>Workshop Presentation Deck</title>
<link href="https://fonts.googleapis.com/css2?family=Cinzel:wght@400;600;700&family=Montserrat:wght@400;500;600;700;800&display=swap" rel="stylesheet">
<style>
:root{
  --orange:#f39a1f;
  --amber:#f9bd2e;
  --teal:#1d4a4e;
  --teal-mid:#2e6367;
  --purple:#6a2150;
  --ink:#2b2b2b;
  --muted:#666;
  --panel:#f1f1f1;
  --page-bg:#ececec;
  --white:#fff;
}
*{box-sizing:border-box;margin:0;padding:0}
html,body{width:1200px;height:2323px;overflow:hidden}
body{position:relative;background:var(--page-bg);font-family:'Montserrat',sans-serif;color:var(--ink)}
.abs{position:absolute}
.hero{position:absolute;left:0;top:0;width:1200px;height:489px;background:linear-gradient(160deg,#cfcfcf 0%,#b9b9b9 45%,#dcdcdc 100%)}
.hero-title{position:absolute;left:72px;top:180px;font-weight:800;font-size:63px;color:var(--orange);letter-spacing:-1px}
.hero-sub{position:absolute;left:196px;top:243px;font-weight:400;font-size:62px;color:#1e1e1e}
.slide{position:absolute;width:383px;height:215px;overflow:hidden;background:var(--white)}
.serif{font-family:'Cinzel',serif}
.title{font-family:'Cinzel',serif;font-weight:700;color:var(--teal);font-size:15px;letter-spacing:-.3px;line-height:1}
.kicker{font-size:5px;letter-spacing:2.2px;color:var(--ink);margin-top:3px}
.tiny{font-size:4.3px;line-height:1.45;color:var(--muted)}
.tiny-w{font-size:4.3px;line-height:1.45;color:#f4f4f4}
.label{font-size:5px;font-weight:600;color:var(--ink)}
.brand{display:flex;align-items:center;gap:3px;font-family:'Cinzel',serif;font-weight:600;color:var(--orange);white-space:nowrap}
.brand i{display:block;border-radius:50%;border:1.5px solid var(--orange)}
.brand-sm{position:absolute;top:6px;right:10px;font-size:5px}
.brand-sm i{width:9px;height:9px}
.copy{position:absolute;left:10px;bottom:7px;font-size:3.4px;letter-spacing:1.4px;color:#777}
.page{position:absolute;right:8px;bottom:5px;display:flex;align-items:center;gap:3px;font-size:3.6px;letter-spacing:1.4px;color:#777}
.page b{display:flex;align-items:center;justify-content:center;width:9px;height:9px;border-radius:50%;background:#333;color:#fff;font-size:4px;font-weight:600;letter-spacing:0}
.photo{position:absolute}
.pill{position:absolute;height:7px;border-radius:4px;font-size:4.3px;font-weight:600;color:#fff;padding-left:5px;line-height:7px}
.dot{position:absolute;width:12px;height:12px;border-radius:50%;background:linear-gradient(135deg,var(--amber),var(--orange));box-shadow:0 0 0 2px #fde6bd;color:#fff;font-size:4px;font-weight:700;display:flex;align-items:center;justify-content:center}
.card{position:absolute;color:#fff;padding:38px 9px 0}
.card h4{font-size:5.5px;font-weight:600;margin-bottom:6px;text-align:center}
.agenda li{list-style:none;display:flex;gap:12px;font-family:'Cinzel',serif;font-size:5.5px;color:#555;border-bottom:.5px solid #ddd;padding:3px 0 2px}
.agenda li span{width:8px}
.check{font-size:4.6px;font-weight:600;color:var(--ink);display:flex;gap:6px;align-items:center;margin-bottom:7px}
.check i{width:6px;height:6px;border:1px solid var(--orange);border-radius:1px;position:relative}
.check i::after{content:"";position:absolute;left:1px;top:-1px;width:2px;height:4px;border:solid var(--orange);border-width:0 1px 1px 0;transform:rotate(40deg)}
.sub-item{font-size:4.5px;font-weight:500;color:var(--ink);margin:0 0 8px 28px;display:flex;gap:6px}
.sub-item::before{content:"";border-left:4px solid var(--orange);border-top:2.5px solid transparent;border-bottom:2.5px solid transparent}
.num-item{position:absolute;width:100px}
.num-item .label{margin-left:20px}
.num-item .tiny{margin-left:20px;width:70px}
.num-item .dot{left:0;top:2px}
.orange-fill{background:linear-gradient(180deg,var(--amber) 0%,var(--orange) 100%)}
</style>
</head>
<body>

<section class="hero" role="img" aria-label="Faded photo of a group of friends raising their hands against a sunset sky"></section>
<div class="hero-title">Presentation</div>
<div class="hero-sub">Deck</div>

<!-- featured title slide -->
<div class="slide" style="left:562px;top:86px;transform:scale(1.2245);transform-origin:0 0">
  <div class="photo" style="left:0;top:0;width:383px;height:167px;background:linear-gradient(180deg,#6d8f91 0%,#44696b 45%,#284648 72%,#5d7778 100%)" role="img" aria-label="Mountain lake with a person sitting on a dock"></div>
  <div class="abs serif" style="left:0;top:82px;width:383px;text-align:center;color:#fff;font-weight:700;font-size:17px">PRESENTATION TITLE</div>
  <div class="abs" style="left:0;top:103px;width:383px;text-align:center;color:#fff;font-size:6px">SUBTITLE GOES HERE</div>
  <div class="abs" style="left:164px;top:155px;width:107px;height:12px;background:var(--teal);border-radius:5px 5px 0 0;color:#fff;font-size:6px;letter-spacing:1px;text-align:center;line-height:12px">April 2020</div>
  <div class="brand abs" style="left:162px;top:184px;font-size:8px"><i style="width:14px;height:14px"></i>MARA ELLISON</div>
</div>

<!-- row 1 -->
<div class="slide" style="left:12px;top:489px">
  <div class="photo" style="left:0;top:0;width:383px;height:167px;background:linear-gradient(180deg,#6d8f91 0%,#44696b 45%,#284648 72%,#5d7778 100%)" role="img" aria-label="Mountain lake with a person sitting on a dock"></div>
  <div class="abs serif" style="left:0;top:82px;width:383px;text-align:center;color:#fff;font-weight:700;font-size:17px">PRESENTATION TITLE</div>
  <div class="abs" style="left:0;top:103px;width:383px;text-align:center;color:#fff;font-size:6px">SUBTITLE GOES HERE</div>
  <div class="abs" style="left:148px;top:155px;width:107px;height:12px;background:var(--teal);border-radius:5px 5px 0 0;color:#fff;font-size:6px;letter-spacing:1px;text-align:center;line-height:12px">April 2020</div>
  <div class="brand abs" style="left:148px;top:184px;font-size:7px"><i style="width:14px;height:14px"></i>MARA ELLISON</div>
</div>

<div class="slide" style="left:408px;top:489px">
  <div class="abs orange-fill" style="left:0;top:0;width:383px;height:181px" role="img" aria-label="Amber background with soft circle pattern"></div>
  <div class="abs serif" style="left:23px;top:84px;color:#fff;font-weight:700;font-size:17px">PRESENTATION TITLE</div>
  <div class="abs" style="left:23px;top:104px;color:#fff;font-size:5px;letter-spacing:2.5px">SUB TITLE GOES HERE</div>
  <div class="brand abs" style="left:25px;top:193px;font-size:6px"><i style="width:14px;height:14px"></i>MARA ELLISON</div>
</div>

<div class="slide" style="left:805px;top:489px;background:linear-gradient(180deg,#2b2b2b,#1c1c1c)" role="img" aria-label="Dark background with subtle circle pattern">
  <div class="brand abs" style="left:110px;top:30px;font-size:12px;color:#fff"><i style="width:24px;height:24px;border-color:#fff"></i>MARA ELLISON</div>
  <div class="abs serif" style="left:0;top:101px;width:383px;text-align:center;color:#fff;font-weight:700;font-size:14px">GENERAL INFORMATION</div>
  <div class="abs" style="left:0;top:196px;width:383px;text-align:center;color:#ccc;font-size:4px">www.maraellison.example</div>
</div>

<!-- row 2 -->
<div class="slide" style="left:12px;top:719px">
  <svg class="abs" style="left:0;top:0" width="383" height="110" viewBox="0 0 383 110" role="img" aria-label="Teal banner over a faded lake photo">
    <path d="M0 0H383V70Q383 82 370 82H80Q30 82 20 90L0 102Z" fill="#1d4a4e"/>
  </svg>
  <div class="abs serif" style="left:0;top:24px;width:370px;text-align:center;color:var(--orange);font-weight:700;font-size:21px">MARA ELLISON</div>
  <div class="abs" style="left:0;top:51px;width:370px;text-align:center;color:#fff;font-size:9px">Add title here</div>
  <div class="abs" style="left:177px;top:70px;display:flex;gap:2px"><i style="width:6px;height:6px;border-radius:50%;background:#fff"></i><i style="width:6px;height:6px;border-radius:50%;background:#fff"></i><i style="width:6px;height:6px;border-radius:50%;background:#fff"></i></div>
  <div class="abs" style="left:283px;top:62px;width:64px;height:64px;border-radius:50%;background:linear-gradient(160deg,#c9a47d,#8a6a4c);border:2px solid #fff" role="img" aria-label="Portrait of the coach"></div>
  <div class="abs serif" style="left:17px;top:124px;font-size:8px;color:var(--ink)">MARA ELLISON</div>
  <p class="abs tiny" style="left:17px;top:135px;width:220px">Neque porro quisquam est, qui dolorem ipsum quia dolor sit amet, consectetur, adipisci velit, sed quia non numquam eius modi tempora incidunt ut labore et dolore magnam aliquam quaerat voluptatem. Ut enim ad minima veniam, quis nostrum exercitationem ullam corporis suscipit laboriosam, nisi ut aliquid ex ea commodi consequatur quis autem vel eum iure reprehenderit.</p>
  <div class="abs" style="left:260px;top:146px;font-size:6.5px;color:var(--ink)">✉ mara@ellisonmail.example</div>
  <div class="abs" style="left:260px;top:157px;font-size:6.5px;color:var(--ink)">☏ 0044 555 010 2233</div>
  <div class="abs" style="left:350px;top:202px;font-size:4px;color:#777">3</div>
</div>

<div class="slide" style="left:408px;top:719px">
  <div class="photo" style="left:15px;top:16px;width:150px;height:180px;background:linear-gradient(160deg,#f2f2f0,#d8d6d2 60%,#bdb9b3)" role="img" aria-label="Desk with laptop and open notebook"></div>
  <div class="abs serif" style="left:81px;top:95px;width:100px;height:30px;background:#fff;font-size:18px;color:var(--ink);text-align:center;line-height:30px">AGENDA</div>
  <div class="brand-sm brand"><i></i>MARA ELLISON</div>
  <ul class="abs agenda" style="left:200px;top:45px;width:150px">
    <li><span>I.</span>Introduction</li><li><span>II.</span>About Us</li><li><span>III.</span>Welcome Message</li><li><span>IV.</span>Company Profile</li><li><span>V.</span>Team</li><li><span>VI.</span>Team Group</li><li><span>VII.</span>Portfolio</li><li><span>VIII.</span>Info Graphic</li><li><span>IX.</span>Contact Us</li>
  </ul>
  <div class="copy">COPYRIGHT © 2020</div><div class="page">PAGE <b>5</b></div>
</div>

<div class="slide" style="left:805px;top:719px">
  <div class="brand-sm brand"><i></i>MARA ELLISON</div>
  <div class="photo" style="left:48px;top:42px;width:102px;height:130px;border-radius:8px;background:linear-gradient(170deg,#a88a5b,#6f5a3b)" role="img" aria-label="Portrait of the coach"></div>
  <div class="abs" style="left:90px;top:143px;width:75px;height:13px;background:var(--teal);border-radius:0 0 6px 0;color:#fff;font-family:'Cinzel',serif;font-size:6px;line-height:13px;text-align:center">YOUR NAME</div>
  <div class="abs title" style="left:190px;top:33px;font-size:14px">WELCOME MESSAGE</div>
  <div class="abs" style="left:188px;top:60px;font-size:30px;color:#ddd;font-family:Georgia,serif">“</div>
  <p class="abs tiny" style="left:192px;top:75px;width:175px">Lorem ipsum dolor sit amet, consectetur adipiscing elit, sed do eiusmod tempor incididunt ut labore et dolore magna aliqua. Lorem ipsum dolor sit amet, consectetur adipiscing elit, sed do eiusmod tempor incididunt ut labore.</p>
  <p class="abs tiny" style="left:192px;top:122px;width:175px">Lorem ipsum dolor sit amet, consectetur adipiscing elit, sed do eiusmod tempor incididunt ut labore et dolore magna aliqua. Lorem ipsum dolor sit amet, consectetur adipiscing elit, sed do eiusmod tempor incididunt ut labore et dolore magna aliqua. Lorem ipsum dolor sit amet, consectetur adipiscing elit, sed do eiusmod tempor incididunt ut labore et dolore magna aliqua.</p>
  <div class="copy">COPYRIGHT © 2020</div><div class="page">PAGE <b>6</b></div>
</div>

<!-- row 3 -->
<div class="slide" style="left:12px;top:948px">
  <div class="brand-sm brand"><i></i>MARA ELLISON</div>
  <div class="abs title" style="left:26px;top:85px;font-size:17px;line-height:1.2">MISSION,<br>VISION &amp;<br>GOAL</div>
  <div class="abs" style="left:198px;top:35px;width:20px;height:14px;border-radius:3px;background:#ddd" role="img" aria-label="Handshake icon"></div>
  <div class="abs serif" style="left:234px;top:35px;font-size:5.5px;font-weight:700">FREE INTRODUCTORY SESSION</div>
  <p class="abs tiny" style="left:234px;top:44px;width:130px">"I'm interested in finding out how coaching can help me meet my goals."</p>
  <div class="abs orange-fill" style="left:177px;top:75px;width:206px;height:74px;border-radius:10px 0 0 10px"></div>
  <div class="abs" style="left:200px;top:105px;width:18px;height:14px;border-radius:3px;border:1.5px solid #fff" role="img" aria-label="Binoculars icon"></div>
  <div class="abs serif" style="left:234px;top:95px;font-size:5.5px;font-weight:700;color:#fff">DISCOVERY SESSION</div>
  <p class="abs tiny-w" style="left:234px;top:104px;width:135px">"I know coaching is for me. Let's get started, get to know each other better, and create the partnership that will help me meet my goals."</p>
  <div class="abs" style="left:198px;top:160px;width:20px;height:20px;border-radius:3px;background:#ddd" role="img" aria-label="Climbing steps icon"></div>
  <div class="abs serif" style="left:234px;top:160px;font-size:5.5px;font-weight:700">COACHING SESSION</div>
  <p class="abs tiny" style="left:234px;top:169px;width:135px">"We are an established coaching team and I want to continue our coaching to accomplish more goals."</p>
  <div class="copy">COPYRIGHT © 2020</div><div class="page">PAGE <b>7</b></div>
</div>

<div class="slide" style="left:408px;top:948px">
  <div class="brand-sm brand"><i></i>MARA ELLISON</div>
  <div class="abs" style="left:56px;top:64px;width:164px;height:46px;background:#fff;box-shadow:0 2px 8px rgba(0,0,0,.12);border-radius:4px;padding:6px 8px">
    <div class="label">Lorem ipsum dolor sit amet</div>
    <p class="tiny" style="margin-top:3px">Lorem ipsum dolor sit amet, consectetur adipiscing elit, sed do eiusmod tempor incididunt ut labore et dolore magna aliqua. Lorem ipsum dolor sit amet.</p>
  </div>
  <div class="abs" style="left:168px;top:60px;width:44px;height:7px;border-radius:4px;background:#9aa0b4"></div>
  <div class="abs" style="left:24px;top:131px;width:164px;height:46px;background:#fff;box-shadow:0 2px 8px rgba(0,0,0,.12);border-radius:4px;padding:6px 8px">
    <div class="label" style="color:var(--orange)">Lorem ipsum dolor sit amet</div>
    <p class="tiny" style="margin-top:3px">Lorem ipsum dolor sit amet, consectetur adipiscing elit, sed do eiusmod tempor incididunt ut labore et dolore magna aliqua. Lorem ipsum dolor sit amet.</p>
  </div>
  <div class="abs" style="left:131px;top:127px;width:44px;height:7px;border-radius:4px;background:var(--amber)"></div>
  <div class="abs" style="left:279px;top:60px;width:40px;height:40px;border-radius:50%;border:3px solid var(--orange)"></div>
  <div class="abs serif" style="left:233px;top:110px;width:140px;text-align:center;color:var(--orange);font-weight:700;font-size:15px">MARA ELLISON</div>
  <div class="copy">COPYRIGHT © 2020</div><div class="page">PAGE <b>8</b></div>
</div>

<div class="slide" style="left:805px;top:948px">
  <div class="abs title" style="left:19px;top:22px;font-size:11px">TEXT, PICTURE AND A QUOTE</div>
  <div class="abs kicker" style="left:21px;top:33px;font-size:4.6px">SUB TITLE GOES HERE</div>
  <div class="abs" style="left:18px;top:20px;width:2px;height:16px;background:var(--teal)"></div>
  <p class="abs tiny" style="left:21px;top:70px;width:172px">Business valuation is a process and a set of procedures used to estimate the economic value of an owner's interest in a business. Valuation is used by financial market participants to determine the price they are willing to pay or receive to effect a sale of a business.</p>
  <p class="abs tiny" style="left:21px;top:124px;width:172px">In addition to estimating the selling price of a business, the same valuation tools are often used by business appraisers to resolve disputes related to estate and gift taxation, divorce litigation, allocate business purchase price among business assets, establish a formula for estimating the value of partners' ownership interest for buy-sell agreements, and many other business and legal purposes such as in shareholders deadlock and estate contest.</p>
  <div class="photo" style="left:212px;top:0;width:146px;height:215px;background:linear-gradient(180deg,#cfd3d3 0%,#b9bdbc 50%,#6d6f6a 100%)" role="img" aria-label="Hiker walking a misty stone path"></div>
  <div class="abs" style="left:212px;top:147px;width:150px;height:46px;background:rgba(29,74,78,.85);padding:8px 6px"><p class="tiny-w">Business valuation is a process and a set of procedures used to estimate the economic value of an owner's interest.</p></div>
  <div class="abs" style="left:362px;top:147px;width:21px;height:46px;background:var(--teal)"></div>
  <div class="copy">COPYRIGHT © 2020</div>
</div>

<!-- row 4 -->
<div class="slide" style="left:12px;top:1177px">
  <div class="brand-sm brand"><i></i>MARA ELLISON</div>
  <div class="photo" style="left:25px;top:0;width:146px;height:192px;border-radius:0 0 8px 12px;background:linear-gradient(180deg,#d3d6d6 0%,#bfc3c2 50%,#6c6e69 100%)" role="img" aria-label="Hiker walking a misty stone path"></div>
  <div class="abs title" style="left:204px;top:36px;font-size:16px">YOUR TEXT HERE</div>
  <div class="abs kicker" style="left:207px;top:50px">SUB TITLE GOES HERE</div>
  <div class="abs" style="left:193px;top:76px">
    <div class="check"><i></i>Lorem ipsum dolor sit amet consectetur adipiscing elit</div>
    <div class="check"><i></i>Lorem ipsum dolor sit consectetur adipiscing elit</div>
    <div class="check"><i></i>Consectetur adipiscing elit</div>
    <div class="sub-item">Lorem ipsum dolor sit consectetur adipiscing elit</div>
    <div class="sub-item">Lorem ipsum dolor sit consectetur adipiscing elit</div>
    <div class="sub-item">Lorem ipsum dolor sit consectetur adipiscing elit</div>
  </div>
  <div class="copy">COPYRIGHT © 2020</div><div class="page">PAGE <b>10</b></div>
</div>

<div class="slide" style="left:408px;top:1177px">
  <div class="brand-sm brand"><i></i>MARA ELLISON</div>
  <div class="abs title" style="left:19px;top:21px;font-size:17px">5 STEPS</div>
  <svg class="abs" style="left:0;top:0" width="383" height="215" viewBox="0 0 383 215"><path d="M10 122 C30 112 70 100 107 105 S135 142 152 140 S200 120 235 134 S300 112 370 115" fill="none" stroke="#ddd" stroke-width="1"/></svg>
  <div class="dot" style="left:29px;top:108px">▤</div>
  <div class="dot" style="left:101px;top:99px">✦</div>
  <div class="dot" style="left:146px;top:134px">➚</div>
  <div class="dot" style="left:229px;top:128px">◎</div>
  <div class="dot" style="left:335px;top:107px">∞</div>
  <div class="abs" style="left:95px;top:61px"><div class="label" style="font-weight:500">Project name</div><p class="tiny" style="width:55px">Lorem ipsum is simply dummy unknown printer took a galley of type.</p></div>
  <div class="abs" style="left:22px;top:137px"><div class="label" style="font-weight:500">Project name</div><p class="tiny" style="width:55px">Lorem ipsum is simply dummy unknown printer took a galley of type.</p></div>
  <div class="abs" style="left:141px;top:165px"><div class="label" style="font-weight:500">Project name</div><p class="tiny" style="width:45px">Lorem ipsum is simply dummy printer took a galley of type.</p></div>
  <div class="abs" style="left:224px;top:88px"><div class="label" style="font-weight:500">Project name</div><p class="tiny" style="width:55px">Lorem ipsum is simply dummy unknown printer took a galley of type.</p></div>
  <div class="abs" style="left:327px;top:148px"><div class="label" style="font-weight:500">Project name</div><p class="tiny" style="width:45px">Lorem ipsum is simply dummy printer took a galley of type.</p></div>
  <div class="copy">COPYRIGHT © 2020</div><div class="page">PAGE <b>11</b></div>
</div>

<div class="slide" style="left:805px;top:1177px">
  <div class="brand-sm brand"><i></i>MARA ELLISON</div>
  <div class="abs title" style="left:20px;top:25px;font-size:16px">YOUR TEXT HERE</div>
  <div class="abs kicker" style="left:22px;top:39px">SUB TITLE GOES HERE</div>
  <div class="card" style="left:20px;top:60px;width:98px;height:128px;background:var(--teal)"><h4>Lorem ipsum dolor</h4><p class="tiny-w">Lorem ipsum dolor sit amet, consectetur adipiscing elit, sed do eiusmod tempor incididunt ut labore et dolore magna aliqua.</p></div>
  <div class="card" style="left:143px;top:60px;width:98px;height:128px;background:var(--purple)"><h4>Lorem ipsum dolor</h4><p class="tiny-w">Lorem ipsum dolor sit amet, consectetur adipiscing elit, sed do eiusmod tempor incididunt ut labore et dolore magna aliqua.</p></div>
  <div class="card orange-fill" style="left:267px;top:60px;width:98px;height:128px"><h4>Lorem ipsum dolor</h4><p class="tiny-w">Lorem ipsum dolor sit amet, consectetur adipiscing elit, sed do eiusmod tempor incididunt ut labore et dolore magna aliqua.</p></div>
  <div class="copy">COPYRIGHT © 2020</div><div class="page">PAGE <b>12</b></div>
</div>

<!-- row 5 -->
<div class="slide" style="left:12px;top:1404px">
  <div class="brand-sm brand"><i></i>MARA ELLISON</div>
  <div class="abs orange-fill" style="left:0;top:128px;width:383px;height:87px"></div>
  <div class="abs title" style="left:25px;top:76px;font-size:16px">YOUR TEXT HERE</div>
  <div class="abs kicker" style="left:27px;top:90px">SUB TITLE GOES HERE</div>
  <p class="abs tiny-w" style="left:26px;top:156px;width:148px">Lorem ipsum dolor sit amet, consectetur adipiscing elit, sed do eiusmod tempor incididunt ut labore et dolore magna aliqua. Lorem ipsum dolor sit amet, consectetur adipiscing elit.</p>
  <div class="abs" style="left:222px;top:37px;width:153px;height:160px;border-radius:8px;background:#fff;box-shadow:0 2px 10px rgba(0,0,0,.15);padding:16px 14px">
    <p class="tiny">Lorem ipsum dolor sit amet, consectetur adipiscing elit, sed do eiusmod tempor incididunt ut labore et dolore magna aliqua. Lorem ipsum dolor sit amet, consectetur adipiscing elit, sed do eiusmod tempor incididunt ut labore et dolore magna aliqua.</p>
    <p class="tiny" style="margin-top:10px">Lorem ipsum dolor sit amet, consectetur adipiscing elit, sed do eiusmod tempor incididunt ut labore et dolore magna aliqua. Lorem ipsum dolor sit amet, consectetur adipiscing elit, sed do eiusmod tempor incididunt ut labore.</p>
  </div>
</div>

<div class="slide" style="left:408px;top:1404px">
  <div class="abs" style="left:0;top:0;width:125px;height:215px;background:var(--teal)"></div>
  <div class="abs serif" style="left:15px;top:34px;color:#fff;font-weight:700;font-size:11.5px;line-height:1.15">PROGRAM<br>CONTEXT AND<br>DELIVERABLES<br>SLIDE</div>
  <p class="abs tiny-w" style="left:15px;top:115px;width:100px">Lorem ipsum dolor sit amet, consectetur adipiscing elit, sed do eiusmod tempor incididunt ut labore et dolore magna aliqua. Lorem ipsum dolor sit amet, consectetur adipiscing elit, sed do eiusmod tempor incididunt ut labore et dolore magna aliqua. Ut enim ad minim veniam, quis nostrud exercitation ullamco laboris nisi ut aliquip.</p>
  <div class="photo" style="left:125px;top:0;width:130px;height:215px;background:linear-gradient(100deg,#2d3a30 0%,#4c5d4d 45%,#b8c2bb 55%,#3d4b3f 100%)" role="img" aria-label="Person standing before a forest waterfall"></div>
  <div class="brand-sm brand"><i></i>MARA ELLISON</div>
  <div class="abs" style="left:265px;top:42px;width:108px">
    <div class="serif" style="font-size:4.8px;font-weight:700">STRATEGY FOR ONLINE LEARNING</div>
    <p class="tiny">Lorem ipsum dolor sit amet, consectetur adipiscing elit, sed do eiusmod tempor incididunt ut labore et dolore magna aliqua. Lorem ipsum dolor sit amet.</p>
    <div class="serif" style="font-size:4.8px;font-weight:700;margin-top:10px">STRATEGY FOR ONLINE LEARNING</div>
    <p class="tiny">Lorem ipsum dolor sit amet, consectetur adipiscing elit, sed do eiusmod tempor incididunt ut labore et dolore magna aliqua. Lorem ipsum dolor sit amet.</p>
    <div class="serif" style="font-size:4.8px;font-weight:700;margin-top:10px">STRATEGY FOR ONLINE LEARNING</div>
    <p class="tiny">Lorem ipsum dolor sit amet, consectetur adipiscing elit, sed do eiusmod tempor incididunt ut labore et dolore magna aliqua. Lorem ipsum dolor sit amet.</p>
  </div>
  <div class="page">PAGE <b>14</b></div>
</div>

<div class="slide" style="left:805px;top:1404px">
  <div class="brand-sm brand"><i></i>MARA ELLISON</div>
  <div class="abs title" style="left:14px;top:22px;font-size:16px">YOUR TEXT HERE</div>
  <div class="abs kicker" style="left:17px;top:36px">SUB TITLE GOES HERE</div>
  <p class="abs tiny" style="left:17px;top:58px;width:352px">Lorem ipsum dolor sit amet, consectetur adipiscing elit, sed do eiusmod tempor incididunt ut labore et dolore magna aliqua. Lorem ipsum dolor sit amet, consectetur adipiscing elit, sed do eiusmod tempor incididunt ut labore et dolore magna aliqua. Ut enim ad minim veniam, quis nostrud exercitation ullamco laboris nisi ut aliquip.</p>
  <p class="abs tiny" style="left:17px;top:84px;width:352px">Lorem ipsum dolor sit amet, consectetur adipiscing elit, sed do eiusmod tempor incididunt ut labore et dolore magna aliqua. Lorem ipsum dolor sit amet, consectetur adipiscing elit, sed do eiusmod tempor incididunt ut labore et dolore magna aliqua.</p>
  <div class="abs serif" style="left:16px;top:110px;font-size:8px;font-weight:700;color:var(--teal)">QUESTIONS / COMMENTS</div>
  <div class="abs" style="left:0;top:121px;width:383px;height:72px;background:var(--panel)"></div>
  <div class="abs" style="left:27px;top:127px"><div class="dot" style="left:0;top:3px;width:10px;height:10px">→</div><div style="margin-left:20px"><div class="serif" style="font-size:5px;font-weight:700;color:var(--orange)">PROJECT NAME</div><p class="tiny" style="width:110px">Lorem ipsum is simply dummy unknown printer took a galley of type and scrambled it to make.</p></div></div>
  <div class="abs" style="left:27px;top:158px"><div class="dot" style="left:0;top:3px;width:10px;height:10px">→</div><div style="margin-left:20px"><div class="serif" style="font-size:5px;font-weight:700;color:var(--orange)">PROJECT NAME</div><p class="tiny" style="width:110px">Lorem ipsum is simply dummy unknown printer took a galley of type and scrambled it to make.</p></div></div>
  <div class="abs" style="left:227px;top:127px"><div class="dot" style="left:0;top:3px;width:10px;height:10px">→</div><div style="margin-left:20px"><div class="serif" style="font-size:5px;font-weight:700;color:var(--orange)">PROJECT NAME</div><p class="tiny" style="width:110px">Lorem ipsum is simply dummy unknown printer took a galley of type and scrambled it to make.</p></div></div>
  <div class="abs" style="left:227px;top:158px"><div class="dot" style="left:0;top:3px;width:10px;height:10px">→</div><div style="margin-left:20px"><div class="serif" style="font-size:5px;font-weight:700;color:var(--orange)">PROJECT NAME</div><p class="tiny" style="width:110px">Lorem ipsum is simply dummy unknown printer took a galley of type and scrambled it to make.</p></div></div>
  <div class="copy">COPYRIGHT © 2020</div><div class="page">PAGE <b>15</b></div>
</div>

<!-- row 6 -->
<div class="slide" style="left:12px;top:1634px">
  <div class="brand-sm brand"><i></i>MARA ELLISON</div>
  <div class="abs title" style="left:16px;top:24px;font-size:16px">YOUR TEXT HERE</div>
  <div class="abs kicker" style="left:19px;top:38px">SUB TITLE GOES HERE</div>
  <div class="num-item" style="left:18px;top:69px"><div class="dot">01</div><div class="label" style="font-weight:500">Project name</div><p class="tiny">Lorem ipsum is simply dummy unknown printer took a galley of type and scrambled it to make.</p></div>
  <div class="num-item" style="left:18px;top:109px"><div class="dot">02</div><div class="label" style="font-weight:500">Project name</div><p class="tiny">Lorem ipsum is simply dummy unknown printer took a galley of type and scrambled it to make.</p></div>
  <div class="num-item" style="left:18px;top:149px"><div class="dot">03</div><div class="label" style="font-weight:500">Project name</div><p class="tiny">Lorem ipsum is simply dummy unknown printer took a galley of type and scrambled it to make.</p></div>
  <div class="num-item" style="left:141px;top:69px"><div class="dot">04</div><div class="label" style="font-weight:500">Project name</div><p class="tiny">Lorem ipsum is simply dummy unknown printer took a galley of type and scrambled it to make.</p></div>
  <div class="num-item" style="left:141px;top:109px"><div class="dot">05</div><div class="label" style="font-weight:500">Project name</div><p class="tiny">Lorem ipsum is simply dummy unknown printer took a galley of type and scrambled it to make.</p></div>
  <div class="num-item" style="left:141px;top:149px"><div class="dot">06</div><div class="label" style="font-weight:500">Project name</div><p class="tiny">Lorem ipsum is simply dummy unknown printer took a galley of type and scrambled it to make.</p></div>
  <div class="num-item" style="left:265px;top:69px"><div class="dot">07</div><div class="label" style="font-weight:500">Project name</div><p class="tiny">Lorem ipsum is simply dummy unknown printer took a galley of type and scrambled it to make.</p></div>
  <div class="num-item" style="left:265px;top:109px"><div class="dot">08</div><div class="label" style="font-weight:500">Project name</div><p class="tiny">Lorem ipsum is simply dummy unknown printer took a galley of type and scrambled it to make.</p></div>
  <div class="num-item" style="left:265px;top:149px"><div class="dot">09</div><div class="label" style="font-weight:500">Project name</div><p class="tiny">Lorem ipsum is simply dummy unknown printer took a galley of type and scrambled it to make.</p></div>
  <div class="copy">COPYRIGHT © 2020</div><div class="page">PAGE <b>16</b></div>
</div>

<div class="slide" style="left:408px;top:1634px">
  <div class="brand-sm brand"><i></i>MARA ELLISON</div>
  <svg class="abs" style="left:0;top:0" width="383" height="215" viewBox="0 0 383 215" fill="none" stroke="#cfcfcf" stroke-width=".8">
    <path d="M28 0 V30 Q28 45 45 45 H345 Q360 45 360 68 Q360 92 340 92 H45 Q25 92 25 118 Q25 140 45 140 H345 Q365 140 365 190 V215"/>
    <circle cx="79" cy="45" r="2.5" fill="#f39a1f" stroke="none"/><circle cx="167" cy="45" r="2.5" fill="#f39a1f" stroke="none"/><circle cx="257" cy="45" r="2.5" fill="#1d4a4e" stroke="none"/>
    <circle cx="79" cy="108" r="2.5" fill="#6a2150" stroke="none"/><circle cx="167" cy="108" r="2.5" fill="#1d4a4e" stroke="none"/><circle cx="257" cy="108" r="2.5" fill="#f39a1f" stroke="none"/>
    <circle cx="167" cy="170" r="2.5" fill="#f39a1f" stroke="none"/><circle cx="257" cy="170" r="2.5" fill="#6a2150" stroke="none"/>
  </svg>
  <div class="abs title" style="left:0;top:12px;width:383px;text-align:center;font-size:15px">YOUR TEXT HERE</div>
  <div class="abs kicker" style="left:0;top:25px;width:383px;text-align:center">SUB TITLE GOES HERE</div>
  <div class="pill" style="left:76px;top:52px;width:55px;background:var(--amber)">Project name</div>
  <div class="pill" style="left:163px;top:52px;width:55px;background:var(--amber)">Project name</div>
  <div class="pill" style="left:253px;top:52px;width:55px;background:var(--teal)">Project name</div>
  <div class="pill" style="left:76px;top:115px;width:55px;background:var(--purple)">Project name</div>
  <div class="pill" style="left:163px;top:115px;width:55px;background:var(--teal)">Project name</div>
  <div class="pill" style="left:253px;top:115px;width:55px;background:var(--amber)">Project name</div>
  <div class="pill" style="left:163px;top:177px;width:55px;background:var(--amber)">Project name</div>
  <div class="pill" style="left:253px;top:177px;width:55px;background:var(--purple)">Project name</div>
  <p class="abs tiny" style="left:78px;top:62px;width:50px">Lorem ipsum is simply dummy unknown printer took a galley.</p>
  <p class="abs tiny" style="left:165px;top:62px;width:50px">Lorem ipsum is simply dummy unknown printer took a galley.</p>
  <p class="abs tiny" style="left:255px;top:62px;width:50px">Lorem ipsum is simply dummy unknown printer took a galley.</p>
  <p class="abs tiny" style="left:78px;top:125px;width:50px">Lorem ipsum is simply dummy unknown printer took a galley.</p>
  <p class="abs tiny" style="left:165px;top:125px;width:50px">Lorem ipsum is simply dummy unknown printer took a galley.</p>
  <p class="abs tiny" style="left:255px;top:125px;width:50px">Lorem ipsum is simply dummy unknown printer took a galley.</p>
  <p class="abs tiny" style="left:165px;top:187px;width:75px">Lorem ipsum is simply dummy unknown printer took a galley.</p>
  <p class="abs tiny" style="left:255px;top:187px;width:75px">Lorem ipsum is simply dummy unknown printer took a galley.</p>
  <div class="copy">COPYRIGHT © 2020</div><div class="page">PAGE <b>17</b></div>
</div>

<div class="slide orange-fill" style="left:805px;top:1634px" role="img" aria-label="Amber section background with soft circle pattern">
  <div class="abs serif" style="left:0;top:160px;width:366px;text-align:right;color:#fff;font-weight:700;font-size:15px">PRESENTATION SECTION BREAK</div>
  <div class="abs" style="left:240px;top:180px;width:22px;height:.8px;background:#fff"></div>
  <div class="abs" style="left:0;top:176px;width:366px;text-align:right;color:#fff;font-size:8px;letter-spacing:2.5px">TITLE GOES HERE</div>
  <div class="abs" style="left:170px;top:203px;color:#fff;font-size:3.5px">www.maraellison.example</div>
  <div class="abs" style="right:8px;bottom:5px;color:#fff;font-size:3.6px;letter-spacing:1.4px">PAGE 18</div>
</div>

<!-- row 7 -->
<div class="slide" style="left:12px;top:1866px">
  <div class="abs" style="left:195px;top:0;width:188px;height:215px;background:var(--panel)"></div>
  <div class="abs title" style="left:20px;top:80px;font-size:16px">YOUR TEXT HERE</div>
  <div class="abs kicker" style="left:22px;top:94px">SUB TITLE GOES HERE</div>
  <div class="abs label" style="left:22px;top:117px;font-size:4.6px">Lorem Ipsum the printing</div>
  <p class="abs tiny" style="left:22px;top:125px;width:150px">Lorem Ipsum the printing and typesetting industry. Lorem Ipsum has been the industry's standard dummy text ever since the 1500s, when an unknown printer took a galley of type and scrambled it to make a type specimen book.</p>
  <p class="abs tiny" style="left:205px;top:30px;width:168px;text-align:center">Lorem Ipsum the printing and typesetting industry. Lorem Ipsum has been the industry's standard dummy text ever since the 1500s, when an unknown printer took a galley of type and scrambled it to make a type specimen book.</p>
  <svg class="abs" style="left:230px;top:90px" width="110" height="105" viewBox="0 0 110 105">
    <polygon points="46,0 64,0 70,17 40,17" fill="#1d4a4e"/>
    <polygon points="39,19 71,19 78,38 32,38" fill="#2e6367"/>
    <polygon points="31,40 79,40 86,60 24,60" fill="#6a2150"/>
    <polygon points="23,62 87,62 95,82 15,82" fill="#f39a1f"/>
    <polygon points="14,84 96,84 104,104 6,104" fill="#f9bd2e"/>
    <g font-family="Montserrat,sans-serif" font-size="4.5" fill="#fff" text-anchor="middle"><text x="55" y="10">Idea 05</text><text x="55" y="30">Idea 04</text><text x="55" y="52">Idea 03</text><text x="55" y="74">Idea 02</text><text x="55" y="96">Idea 01</text></g>
  </svg>
  <div class="copy">COPYRIGHT © 2020</div><div class="page">PAGE</div>
</div>

<div class="slide" style="left:408px;top:1866px">
  <div class="brand-sm brand"><i></i>MARA ELLISON</div>
  <div class="abs title" style="left:19px;top:24px;font-size:16px">YOUR TEXT HERE</div>
  <div class="abs kicker" style="left:22px;top:38px">SUB TITLE GOES HERE</div>
  <p class="abs" style="left:28px;top:63px;width:205px;font-size:5px;line-height:1.4;color:#444"><b style="color:var(--purple);font-size:8px">#1.</b> We take historic samples of your operations data to identify what current data points being collected has value. We then advise on what metrics should be collected to increase future revenues.</p>
  <p class="abs" style="left:28px;top:107px;width:205px;font-size:5px;line-height:1.4;color:#444"><b style="color:var(--teal);font-size:8px">#2.</b> We use proprietary methods to filter your data, anonymize, add equity mapping, demographic segmentation, and compliance and productize into the niche community of data buyers.</p>
  <p class="abs" style="left:28px;top:156px;width:205px;font-size:5px;line-height:1.4;color:#444"><b style="color:var(--orange);font-size:8px">#3.</b> Once clients verify samples of your data and agree to purchase, we create the compliant legal setting that keeps your privacy as well as the optimal revenue potential for your data.</p>
  <svg class="abs" style="left:240px;top:36px" width="125" height="150" viewBox="0 0 125 150" font-family="Montserrat,sans-serif" font-size="12" font-weight="700">
    <rect x="30" y="95" width="80" height="36" fill="#f39a1f"/><ellipse cx="70" cy="131" rx="40" ry="12" fill="#f39a1f"/><ellipse cx="70" cy="95" rx="40" ry="12" fill="#f9bd2e"/>
    <rect x="25" y="55" width="85" height="36" fill="#1d4a4e"/><ellipse cx="67.5" cy="91" rx="42.5" ry="12" fill="#1d4a4e"/><ellipse cx="67.5" cy="55" rx="42.5" ry="12" fill="#2e6367"/>
    <rect x="3" y="16" width="85" height="38" fill="#6a2150"/><ellipse cx="45.5" cy="54" rx="42.5" ry="12" fill="#6a2150"/><ellipse cx="45.5" cy="16" rx="42.5" ry="12" fill="#551a40"/>
    <text x="40" y="50" fill="#8a3a6c">#1</text><text x="65" y="86" fill="#3f7377">#2</text><text x="68" y="128" fill="#f8c35a">#3</text>
  </svg>
  <div class="copy">COPYRIGHT © 2020</div><div class="page">PAGE <b>20</b></div>
</div>

<div class="slide" style="left:805px;top:1866px">
  <div class="brand-sm brand"><i></i>MARA ELLISON</div>
  <div class="abs title" style="left:20px;top:74px;font-size:14px">STEPS TO SUCCESS</div>
  <div class="abs kicker" style="left:22px;top:87px">SUB TITLE GOES HERE</div>
  <div class="abs" style="left:208px;top:24px;width:34px;height:50px;border-radius:6px;background:linear-gradient(180deg,var(--amber),var(--orange));opacity:.85" role="img" aria-label="Figure stepping up a stair"></div>
  <div class="abs" style="left:32px;top:163px;width:61px;height:15px;background:var(--purple)"></div>
  <div class="abs" style="left:101px;top:140px;width:61px;height:15px;background:var(--teal)"></div>
  <div class="abs" style="left:173px;top:112px;width:61px;height:15px;background:var(--teal)"></div>
  <div class="abs orange-fill" style="left:242px;top:91px;width:61px;height:15px"></div>
  <div class="abs orange-fill" style="left:307px;top:70px;width:61px;height:15px"></div>
  <div class="abs" style="left:16px;top:181px;width:78px"><div class="label" style="font-weight:500">Lorem ipsum dolor</div><p class="tiny">Lorem ipsum dolor sit amet, consectetur adipiscing elit.</p></div>
  <div class="abs" style="left:104px;top:158px;width:62px"><div class="label" style="font-weight:500">Lorem ipsum dolor</div><p class="tiny">Lorem ipsum dolor sit amet, consectetur adipiscing elit.</p></div>
  <div class="abs" style="left:173px;top:130px;width:62px"><div class="label" style="font-weight:500">Lorem ipsum dolor</div><p class="tiny">Lorem ipsum dolor sit amet, consectetur adipiscing elit.</p></div>
  <div class="abs" style="left:244px;top:109px;width:62px"><div class="label" style="font-weight:500">Lorem ipsum dolor</div><p class="tiny">Lorem ipsum dolor sit amet, consectetur adipiscing elit.</p></div>
  <div class="abs" style="left:312px;top:88px;width:62px"><div class="label" style="font-weight:500">Lorem ipsum dolor</div><p class="tiny">Lorem ipsum dolor sit amet, consectetur adipiscing elit.</p></div>
  <div class="copy">COPYRIGHT © 2020</div><div class="page">PAGE <b>21</b></div>
</div>

<!-- row 8 -->
<div class="slide" style="left:216px;top:2094px">
  <div class="brand abs" style="left:15px;top:55px;font-size:7px"><i style="width:15px;height:15px"></i>MARA ELLISON</div>
  <div class="abs title" style="left:14px;top:94px;font-size:18px;color:var(--ink);font-weight:400">PRESENTATION TITLE</div>
  <div class="abs" style="left:15px;top:115px;font-size:5.5px">SUB TITLE GOES HERE</div>
  <div class="abs" style="left:0;top:175px;width:383px;height:40px;background:var(--teal)"></div>
</div>

<div class="slide" style="left:613px;top:2094px">
  <div class="brand abs" style="left:15px;top:55px;font-size:7px"><i style="width:15px;height:15px"></i>MARA ELLISON</div>
  <div class="abs title" style="left:14px;top:94px;font-size:18px;color:var(--ink);font-weight:400">PRESENTATION TITLE</div>
  <div class="abs" style="left:15px;top:115px;font-size:5.5px">SUB TITLE GOES HERE</div>
  <div class="abs" style="left:0;top:175px;width:383px;height:40px;background:var(--purple)"></div>
</div>

</body>
</html>
```